WINE LABEL for Oak-Q Vale.

We require a wine bottle label for our Oak-Q Vale brand new to the market.
A sample "mock-up" layout of the front and back label is attached. The Oak-Q writing can be a logo type design with any font the designer chooses keeping in mind this will be used on Stationary, business cards and vehicles as well so could included some creative design as long as its clear to read the "Oak-Q" We require a pair of "crusty cowboy boots" as the main theme of the label but the designer could use flair here and design inside a circle or leave as set out.The main thing is they are rugged looking. The label can be framed if appropriate and the use of a parchment look or old western looking idea could be used. We would limit colors to 3 for printing purposes so the combination of colors is up to the designer as long as it stands out on the label visually. The rear label components is attached but can be set-out in any form the designer chooses. The use of the mountain outline at the base of the rear label may add a nice addition to this as its the view we see from our vineyard. Anything else please message me directly.

Target Market(s)

Boutique vineyard label that stands out from the normal.

Contact Information for Business Card

Set out using the designs from the label.

Font styles to use
Other font styles liked:
• Designer to use their selection

Requirements
Must have
• as set out on attached label Mock-up.
• A western theme for the label is preferred.
Should not have
• photos or more than 3 colours

```html
<!DOCTYPE html>
<html lang="en">
<head>
<meta charset="utf-8">
<title>Oak-Q Vale Pinot Noir Label</title>
<link rel="stylesheet" href="https://fonts.googleapis.com/css2?family=Rye&family=Cormorant+SC:wght@500;600&family=Pinyon+Script&family=Cormorant+Garamond:wght@500&display=swap">
<style>
  :root {
    --backdrop: #2a2a2a;
    --label-paper: #efeee9;
    --label-paper-shade: #e2e0d9;
    --wine-red: #a3302e;
    --saddle-brown: #5b5247;
    --ink-dark: #3b3631;
    --boot-light: #c9c1b3;
    --boot-dark: #8a7e6d;
  }
  * { margin: 0; padding: 0; box-sizing: border-box; }
  html, body {
    width: 1200px;
    height: 2486px;
    overflow: hidden;
    background: var(--backdrop);
  }
  .wine-label {
    position: absolute;
    left: 118px;
    top: 684px;
    width: 965px;
    height: 1118px;
    background: linear-gradient(90deg, var(--label-paper-shade) 0%, var(--label-paper) 18%, var(--label-paper) 82%, var(--label-paper-shade) 100%);
    text-align: center;
  }
  .wine-label > * {
    position: absolute;
    left: 0;
    width: 100%;
  }
  .established {
    top: 30px;
    font-family: "Cormorant Garamond", serif;
    font-size: 22px;
    line-height: 1.05;
    color: var(--ink-dark);
    letter-spacing: 2px;
  }
  .brand-name {
    top: 110px;
    font-family: "Cormorant Garamond", serif;
    font-weight: 500;
    font-size: 84px;
    line-height: 1;
    color: var(--ink-dark);
    letter-spacing: 1px;
  }
  .boots-artwork {
    top: 250px;
    left: 340px;
    width: 285px;
    height: 370px;
    border-radius: 18px;
    background: radial-gradient(ellipse at 50% 55%, var(--boot-dark) 0%, var(--boot-light) 55%, var(--label-paper) 80%);
  }
  .wine-name {
    top: 760px;
    font-family: "Rye", serif;
    font-weight: 400;
    font-size: 80px;
    line-height: 1;
    color: var(--saddle-brown);
    letter-spacing: 3px;
  }
  .varietal {
    top: 868px;
    font-family: "Cormorant SC", serif;
    font-weight: 600;
    font-size: 56px;
    line-height: 1;
    color: var(--wine-red);
    letter-spacing: 1px;
  }
  .vintage {
    top: 936px;
    font-family: "Cormorant Garamond", serif;
    font-weight: 500;
    font-size: 38px;
    line-height: 1;
    color: var(--ink-dark);
    letter-spacing: 3px;
  }
  .region {
    top: 988px;
    font-family: "Pinyon Script", cursive;
    font-size: 56px;
    line-height: 1;
    color: var(--ink-dark);
  }
  .origin {
    top: 1068px;
    font-family: "Cormorant SC", serif;
    font-weight: 500;
    font-size: 25px;
    line-height: 1;
    color: var(--ink-dark);
    letter-spacing: 6px;
  }
</style>
</head>
<body>
  <main class="wine-label">
    <p class="established">EST<br>2007</p>
    <h1 class="brand-name">Oak-Q Vale</h1>
    <div class="boots-artwork" role="img" aria-label="Sketched pair of worn cowboy boots with spurs"></div>
    <h2 class="wine-name">TUSSOCK RIDGE</h2>
    <p class="varietal">Pinot Noir</p>
    <p class="vintage">2016</p>
    <p class="region">North Otago</p>
    <p class="origin">NEW ZEALAND WINE</p>
  </main>
</body>
</html>
```